Info Card

6 ¾ x 4 ¾ info card created, front and back. I have put together a project brief, and we have most of the graphic elements and very straightforward instructions on what is needed on front and back. This is an info card that we’ll include with our product packaging detailing our Damage Protection Plan.
We have a logo for the protection plan which mimics our 8Q Telecom logo colors.
This protection plan is for our product, the KM Stratus – logo attached.

Target Market(s)

B2B

Industry/Entity Type

Telecommunications

Font styles to use
Sans Serif

Colors

Designer to choose colors to be used in the design.

Requirements
Must have
• The text that I included on the brief.
• Must be delivered as a vector file.
Should not have
• no grungy look, nothing "rugged".

```html
<!DOCTYPE html>
<html lang="en">
<head>
<meta charset="utf-8">
<title>8Q Telecom – Damage Protection Plan Info Card</title>
<link rel="stylesheet" href="https://fonts.googleapis.com/css2?family=Oswald:wght@300;400&family=Questrial&family=Raleway:wght@500;600&display=swap">
<style>
:root{
  --purple:#6a4aa0;
  --purple-deep:#5b3c92;
  --navy:#1a3562;
  --navy-text:#1d2a4a;
  --silver-1:#f2f3f5;
  --silver-2:#c9cdd3;
  --silver-3:#e4e6ea;
  --cell-light:#eef0f2;
  --dark-band:#1e1f22;
}
*{margin:0;padding:0;box-sizing:border-box}
html,body{width:1200px;height:845px;overflow:hidden;background:#fff}
.card{position:relative;width:1200px;height:845px;overflow:hidden;
  background:linear-gradient(100deg,var(--silver-2) 0%,var(--silver-1) 22%,#b9bec6 45%,var(--silver-3) 62%,#f7f8fa 78%,#c5c9cf 100%)}
.corner-band{position:absolute;top:0;right:0;width:560px;height:290px}
.coverage{position:absolute;left:45px;top:53px;width:592px;display:grid;
  grid-template-columns:218px 175px 189px;column-gap:5px;
  grid-template-rows:70px 64px 66px 66px 269px 62px 65px 67px;row-gap:3px;
  font-family:"Oswald",sans-serif;font-weight:300;box-shadow:0 0 8px rgba(0,0,0,.35);
  background:#d5d8dc;padding:0}
.head{background:var(--purple);color:#fff;font-size:17px;line-height:1.25;
  display:flex;align-items:center;justify-content:center;text-align:center;letter-spacing:.3px}
.label{background:linear-gradient(90deg,#fdfdfd,#e3e5e8);color:var(--purple);font-size:18px;
  line-height:1.3;text-align:right;padding:0 14px 0 10px;display:flex;flex-direction:column;justify-content:center}
.label small{display:block;color:var(--navy-text);font-size:15.5px;font-weight:400;line-height:1.42;margin-top:2px}
.plan{background:var(--navy);display:flex;align-items:center;justify-content:center}
.warranty{background:linear-gradient(90deg,#e6e8eb,#f6f7f8);display:flex;align-items:center;justify-content:center}
.shield{width:48px;height:53px}
.pitch{position:absolute;left:669px;top:204px;width:466px}
.pitch h1{font-family:"Questrial",sans-serif;font-weight:400;color:var(--purple);
  font-size:36px;line-height:41px;letter-spacing:2.5px}
.pitch .body{margin-top:31px;font-family:"Questrial",sans-serif;color:#2b2f3a;
  font-size:20px;line-height:28px;text-align:justify}
.pitch .cta{margin-top:30px;font-family:"Raleway",sans-serif;font-weight:600;
  color:var(--purple);font-size:20.5px;line-height:29px}
.plan-mark{position:absolute;left:669px;top:715px;display:flex;align-items:center;gap:8px;
  font-family:"Questrial",sans-serif;color:var(--purple);font-size:15px}
.plan-mark i{width:14px;height:14px;background:var(--purple);display:block}
.contact-bar{position:absolute;left:782px;top:697px;width:35px;height:88px;background:var(--purple)}
.contact{position:absolute;left:826px;top:694px;font-family:"Raleway",sans-serif;font-weight:500;
  font-size:21px;line-height:32px;letter-spacing:3px;list-style:none}
.contact .navy{color:var(--navy-text)}
.contact .violet{color:var(--purple)}
</style>
</head>
<body>
<main class="card">
  <svg class="corner-band" viewBox="0 0 560 290" aria-hidden="true">
    <defs>
      <linearGradient id="bandFill" x1="0" y1="0" x2="1" y2="1">
        <stop offset="0" stop-color="#2a2b2f"/><stop offset="1" stop-color="#111214"/>
      </linearGradient>
      <linearGradient id="edge" x1="0" y1="0" x2="1" y2="0">
        <stop offset="0" stop-color="#9a9ea6"/><stop offset=".6" stop-color="#ffffff"/><stop offset="1" stop-color="#8b9098"/>
      </linearGradient>
    </defs>
    <path d="M0 0 C150 40 330 40 560 275 L560 0 Z" fill="url(#edge)"/>
    <path d="M25 0 C170 30 350 35 560 248 L560 0 Z" fill="url(#bandFill)"/>
  </svg>

  <svg width="0" height="0" style="position:absolute" aria-hidden="true">
    <symbol id="tick-shield" viewBox="0 0 48 53">
      <path d="M24 2 C32 6 40 7 46 7 C46 30 38 44 24 51 C10 44 2 30 2 7 C8 7 16 6 24 2 Z" fill="#c4c9d0" stroke="#eef0f3" stroke-width="2"/>
      <path d="M24 7 C31 10 37 11 41 11 C41 29 34 40 24 46 C14 40 7 29 7 11 C11 11 17 10 24 7 Z" fill="#3d6aa8"/>
      <path d="M14 27 L21 34 L35 18" fill="none" stroke="#fff" stroke-width="5" stroke-linecap="round" stroke-linejoin="round"/>
    </symbol>
  </svg>

  <section class="coverage" aria-label="Coverage comparison">
    <div class="head">COVERAGE INCLUDES</div>
    <div class="head">DAMAGE PROTECTION<br>PLAN - 2 YRS</div>
    <div class="head">DEFAULT MANUFACTURER<br>WARRANTY - 1YR</div>

    <div class="label">MANUFACTURER DEFECTS</div>
    <div class="plan"><svg class="shield"><use href="#tick-shield"/></svg></div>
    <div class="warranty"><svg class="shield"><use href="#tick-shield"/></svg></div>

    <div class="label">ACCIDENTAL/<br>ELECTRICAL/WEATHER</div>
    <div class="plan"><svg class="shield"><use href="#tick-shield"/></svg></div>
    <div class="warranty"></div>

    <div class="label">CRACKED ENCLOSURE<br>AND LCD SCREEN</div>
    <div class="plan"><svg class="shield"><use href="#tick-shield"/></svg></div>
    <div class="warranty"></div>

    <div class="label">PREMIUM CALIBRATION<br>($895 VALUE)
      <small>includes full enclosure replacement and sealants, internal calibration, update firmware/software, comprehensive systems test, tune-ups and cleaning</small></div>
    <div class="plan"><svg class="shield"><use href="#tick-shield"/></svg></div>
    <div class="warranty"></div>

    <div class="label">BATTERY REPLACEMENT<br>($595 VALUE)</div>
    <div class="plan"><svg class="shield"><use href="#tick-shield"/></svg></div>
    <div class="warranty"></div>

    <div class="label">TOTAL LOSS<br>REPLACEMENT ($2,000</div>
    <div class="plan"><svg class="shield"><use href="#tick-shield"/></svg></div>
    <div class="warranty"></div>

    <div class="label">PEACE OF MIND</div>
    <div class="plan"><svg class="shield"><use href="#tick-shield"/></svg></div>
    <div class="warranty"></div>
  </section>

  <section class="pitch">
    <h1>IS YOUR<br>INVESTMENT<br>PROTECTED<br>AGAINST ACCIDENTS?</h1>
    <p class="body">Protect your KM Stratus from accidental damages and keep it in top working conditions with 1 Premium Calibration and Battery Replacement (if needed). We even cover total loss damages with a $2,000 deductible.</p>
    <p class="cta">Contact our sales team to learn more or chat with us on our website.</p>
  </section>

  <div class="plan-mark"><i></i>2 Year Plan</div>
  <div class="contact-bar"></div>
  <ul class="contact">
    <li class="navy">www.8qtelecom.com</li>
    <li class="violet">+1 (555) 014-2290</li>
    <li class="navy">sales@8qtelecom.com</li>
  </ul>
</main>
</body>
</html>
```